Hoods and pressure washing

We pressure wash house, driveways, buisnesses, gas stations, restraunt hoods and equipments, fences, construction sites and anything that can be pressure washed

Will like my flyer to have written: licenesed, bonded, and insured up to 2 million.(but professionally written)

Target Market(s)

Restraunts, corporations, houses and apartment complexes

Industry/Entity Type

Construction

Colors
33a6d7
33b8a4
ffffff
3176b5

Requirements
Must have
• Before and after pics of dirty and clean pics
Nice to have
• I would like it to be a one paper flyer could be front or back. Company name is aquaBrite. I like a corner written down with all the work we do. Ex: hoods, sidewalks, sidings, houses etc...
• Contact info: Dennis Cawley, phone# 629-415-3307
• Lou Marten, phone # (didnt get one yet)
• Adress: 2417 E. Brantwood rd, portland, Tn, 37162

```html
<!DOCTYPE html>
<html lang="en">
<head>
<meta charset="utf-8">
<title>aquaBrite – Hoods and Pressure Washing Flyer</title>
<link rel="stylesheet" href="https://fonts.googleapis.com/css2?family=Source+Sans+3:ital,wght@0,400;0,600;0,700;0,900;1,700&family=Source+Serif+4:wght@400&display=swap">
<style>
  :root {
    --sky: #2fa6da;
    --navy: #2a3a93;
    --brand-blue: #1b63b0;
    --teal: #2bb8a3;
    --red: #e8403a;
    --ink: #333333;
    --white: #ffffff;
  }
  html, body { margin: 0; padding: 0; overflow: hidden; }
  body { width: 912px; height: 1200px; background: var(--white); }
  .flyer {
    position: relative; width: 912px; height: 1200px; overflow: hidden;
    background: var(--white);
    font-family: "Source Sans 3", sans-serif; color: var(--white);
  }
  .backdrop { position: absolute; inset: 0; }
  .mascot-art {
    position: absolute; left: 54px; top: 20px; width: 242px; height: 267px;
    background: linear-gradient(160deg, #e9e9e9, #9a9a9a 60%, #d8d8d8);
    border-radius: 6px;
  }
  .brand-name {
    position: absolute; left: 250px; top: 58px; margin: 0;
    font-weight: 900; font-size: 92px; line-height: 1; letter-spacing: -1px;
    color: var(--brand-blue);
  }
  .brand-dot {
    display: inline-block; width: 22px; height: 22px; border-radius: 50%;
    background: var(--brand-blue); margin-left: 10px; vertical-align: 8px;
  }
  .brand-tagline {
    position: absolute; left: 250px; top: 148px; margin: 0;
    font-family: "Source Serif 4", serif; font-size: 33px; color: var(--red);
    letter-spacing: -0.5px;
  }
  .insurance {
    position: absolute; left: 385px; top: 212px; margin: 0;
    font-weight: 600; font-size: 39px; color: var(--ink);
  }
  .price-badge {
    position: absolute; left: 612px; top: 276px; width: 250px; height: 250px;
    border-radius: 50%; background: #3d9bd6;
    display: flex; align-items: center; justify-content: center;
  }
  .price-badge-inner {
    width: 232px; height: 232px; border-radius: 50%; background: var(--red);
    box-shadow: inset 0 0 0 3px rgba(255,255,255,0.85);
    display: flex; flex-direction: column; align-items: center; justify-content: center;
    font-style: italic; font-weight: 700; text-align: center; line-height: 1;
  }
  .price-lead { font-size: 38px; }
  .price-amount { font-style: normal; font-size: 54px; margin: 6px 0 2px; }
  .price-tail { font-size: 38px; }
  .owner {
    position: absolute; left: 47px; top: 384px; margin: 0;
    font-style: italic; font-weight: 700; font-size: 34px;
  }
  .services-title {
    position: absolute; left: 47px; top: 426px; margin: 0;
    font-weight: 700; font-size: 40px;
  }
  .service-list {
    position: absolute; left: 49px; top: 498px; width: 640px; margin: 0; padding: 0;
    list-style: none; display: grid; grid-template-columns: 295px auto;
    row-gap: 9px; font-size: 26px; font-weight: 600; line-height: 29px;
  }
  .service-list li { padding-left: 24px; position: relative; }
  .service-list li::before {
    content: ""; position: absolute; left: 0; top: 9px; width: 13px; height: 13px;
    border-radius: 50%; background: var(--red); box-shadow: 0 0 0 1.5px var(--white);
  }
  .service-list .wide { grid-column: 1 / span 2; }
  .gallery { position: absolute; top: 739px; height: 203px; }
  .gallery-before-after { left: 45px; width: 309px;
    background: linear-gradient(90deg, #4a4a46 0%, #5d5f52 35%, #e6e8ea 40%, #dcdfe3 70%, #6f8c4f 100%); }
  .gallery-deck { left: 361px; width: 228px;
    background: linear-gradient(180deg, #5d8a3c 0%, #6a4a2a 25%, #9a5a2d 70%, #c4733a 100%); }
  .gallery-roof { left: 598px; width: 260px;
    background: linear-gradient(160deg, #c95a2d 0%, #e0733f 55%, #d8d8d8 100%); }
  .photo-label {
    position: absolute; bottom: 22px; font-weight: 700; font-size: 22px;
  }
  .photo-label.before { left: 8px; color: var(--white); }
  .photo-label.after { left: 167px; color: var(--ink); }
  .credentials {
    position: absolute; left: 44px; top: 960px; width: 808px; height: 39px;
    border-radius: 20px; background: var(--white); color: var(--ink);
    text-align: center; font-weight: 600; font-size: 32px; line-height: 39px; margin: 0;
  }
  .contact-name {
    position: absolute; left: 0; top: 1014px; width: 912px; text-align: center; margin: 0;
    font-weight: 600; font-size: 34px;
  }
  .contact-phone {
    position: absolute; left: 0; top: 1054px; width: 912px; text-align: center; margin: 0;
    font-weight: 700; font-size: 62px; line-height: 1;
  }
  .footer-line {
    position: absolute; left: 45px; top: 1138px; width: 820px;
    display: flex; align-items: center; gap: 26px; font-size: 23px; font-weight: 600;
  }
  .footer-dot {
    width: 28px; height: 28px; border-radius: 50%; background: var(--red);
    box-shadow: 0 0 0 2px var(--white);
  }
</style>
</head>
<body>
<main class="flyer">
  <svg class="backdrop" width="912" height="1200" viewBox="0 0 912 1200" aria-hidden="true">
    <path d="M0,338 Q330,284 690,348" fill="none" stroke="var(--teal)" stroke-width="10"/>
    <path d="M0,352 Q330,300 690,358 L912,392 L912,1200 L0,1200 Z" fill="var(--navy)"/>
    <path d="M0,366 Q330,318 690,374 L912,449 L912,1200 L0,1200 Z" fill="var(--sky)"/>
  </svg>

  <div class="mascot-art" role="img" aria-label="Illustration of a worker operating a pressure washer machine"></div>

  <h1 class="brand-name">aquaBrite<span class="brand-dot"></span></h1>
  <p class="brand-tagline">HOODS AND PRESSURE WASHING</p>
  <p class="insurance">Insured up to2 million</p>

  <div class="price-badge">
    <div class="price-badge-inner">
      <span class="price-lead">Prices<br>start at</span>
      <span class="price-amount">$49 .99</span>
      <span class="price-tail">and up</span>
    </div>
  </div>

  <p class="owner">Dennis Cawley’s</p>
  <h2 class="services-title">Pressure Washing Services:</h2>
  <ul class="service-list">
    <li>House / Sidings</li><li>Driveways</li>
    <li>Buisnesses</li><li>Gas Stations</li>
    <li>Fences</li><li>Construction Sites</li>
    <li>Hoods</li><li>Sidewalks</li>
    <li class="wide">Restraunt Hoods And Equipments</li>
    <li class="wide">And anything that can be pressure washed</li>
  </ul>

  <div class="gallery gallery-before-after" role="img" aria-label="Before and after photo of a driveway, dirty half beside clean half, house behind">
    <span class="photo-label before">Before</span>
    <span class="photo-label after">After</span>
  </div>
  <div class="gallery gallery-deck" role="img" aria-label="Photo of a wooden deck being cleaned with a pressure washer wand"></div>
  <div class="gallery gallery-roof" role="img" aria-label="Photo of a worker pressure washing a red tiled roof"></div>

  <p class="credentials">Licenesed Bonded</p>
  <p class="contact-name">Contact&nbsp; Dennis Cawley</p>
  <p class="contact-phone">629-415-3307</p>

  <div class="footer-line">
    <span>Lou Marten: 000 000 0000</span>
    <span class="footer-dot"></span>
    <span>2417 E. Brantwood rd, portland, Tn, 37162</span>
  </div>
</main>
</body>
</html>
```